Business card for exciting VC company

Should look simple, crisp, and modern.

Industry/Entity Type

Venture Capital

Contact Information for Business Card

Would like to see at least one design that has our blue on the back with the tagline "Transforming Traditional Industry" and white front with contact details.

Font styles to use
Sans Serif

Requirements
Must have
• Logo

Gregory Tallis
gtallis@brindlewave.vc
Managing Partner
M (628)354-xxxx

```html
<!DOCTYPE html>
<html lang="en">
<head>
<meta charset="utf-8">
<title>Brindlewave Capital – Business Card</title>
<link rel="stylesheet" href="https://fonts.googleapis.com/css2?family=Montserrat:wght@400;500;600;700&display=swap">
<style>
  :root {
    --brand-blue: #3d72c4;
    --brand-blue-deep: #24549e;
    --brand-blue-light: #5f93d6;
    --ink: #1b1d22;
    --ink-soft: #4a4d55;
    --paper: #ffffff;
    --stage: #e9ebee;
    --divider: #7b7f87;
  }
  * { box-sizing: border-box; margin: 0; padding: 0; }
  html, body {
    width: 1200px;
    height: 800px;
    overflow: hidden;
    background: var(--stage);
    font-family: "Montserrat", sans-serif;
  }
  .sheet {
    width: 1200px;
    height: 800px;
    display: flex;
    align-items: center;
    justify-content: center;
    gap: 48px;
  }
  .card {
    position: relative;
    width: 540px;
    height: 308px;
    overflow: hidden;
    box-shadow: 0 6px 18px rgba(20, 30, 50, 0.14);
  }

  /* Back side */
  .card-back { background: var(--brand-blue); color: var(--paper); }
  .card-back .backdrop {
    position: absolute; inset: 0;
    background: linear-gradient(135deg, var(--brand-blue-light) 0%, var(--brand-blue) 45%, var(--brand-blue-deep) 100%);
  }
  .card-back .wordmark {
    position: absolute;
    left: 0; right: 0; top: 92px;
    text-align: center;
    font-weight: 500;
    letter-spacing: 0.08em;
    text-transform: uppercase;
    line-height: 1.1;
  }
  .card-back .wordmark-name { display: block; font-size: 44px; }
  .card-back .wordmark-sub { display: block; font-size: 14px; letter-spacing: 0.5em; margin-top: 6px; }
  .card-back .tagline {
    position: absolute;
    left: 0; right: 0; bottom: 46px;
    text-align: center;
    font-size: 15px;
    font-weight: 500;
    letter-spacing: 0.06em;
    text-transform: uppercase;
  }

  /* Front side */
  .card-front { background: var(--paper); color: var(--ink); }
  .card-front .wordmark {
    position: absolute;
    left: 40px; top: 118px;
    width: 220px;
    text-align: center;
    font-weight: 600;
    color: var(--ink);
    text-transform: uppercase;
    line-height: 1.1;
  }
  .card-front .wordmark-name { display: block; font-size: 25px; letter-spacing: 0.06em; }
  .card-front .wordmark-sub { display: block; font-size: 9px; letter-spacing: 0.5em; margin-top: 4px; }
  .card-front .divider {
    position: absolute;
    left: 282px; top: 96px;
    width: 1.5px; height: 100px;
    background: var(--divider);
  }
  .contact {
    position: absolute;
    left: 300px; top: 96px;
  }
  .contact-name { font-size: 16px; font-weight: 700; color: var(--ink); }
  .contact-role { font-size: 11.5px; font-weight: 500; color: var(--brand-blue); margin-top: 2px; }
  .contact-list { list-style: none; margin-top: 14px; }
  .contact-list li {
    display: flex; align-items: center; gap: 8px;
    font-size: 12.5px; color: var(--ink-soft);
    line-height: 1.55;
  }
  .contact-list svg { width: 12px; height: 12px; flex: none; }
  .edge-band {
    position: absolute; left: 0; right: 0; bottom: 0;
    height: 14px;
    display: flex;
  }
  .edge-band .band-blue { flex: 7; background: var(--brand-blue); }
  .edge-band .band-black { flex: 3; background: var(--ink); }
</style>
</head>
<body>
<main class="sheet">

  <section class="card card-back" aria-label="Card back">
    <div class="backdrop" role="img" aria-label="Blue-toned photograph looking up at a glass and steel office tower"></div>
    <div class="wordmark">
      <span class="wordmark-name">Brindlewave</span>
      <span class="wordmark-sub">Capital</span>
    </div>
    <p class="tagline">Transforming Traditional Industry</p>
  </section>

  <section class="card card-front" aria-label="Card front">
    <div class="wordmark">
      <span class="wordmark-name">Brindlewave</span>
      <span class="wordmark-sub">Capital</span>
    </div>
    <div class="divider"></div>
    <div class="contact">
      <p class="contact-name">Gregory Tallis</p>
      <p class="contact-role">Managing Partner</p>
      <ul class="contact-list">
        <li>
          <svg viewBox="0 0 12 12" aria-hidden="true"><rect x="3" y="0.8" width="6" height="10.4" rx="1.2" fill="none" stroke="#3d72c4" stroke-width="1.2"/><line x1="5" y1="9.3" x2="7" y2="9.3" stroke="#3d72c4" stroke-width="1"/></svg>
          (628)354-xxxx
        </li>
        <li>
          <svg viewBox="0 0 12 12" aria-hidden="true"><rect x="0.8" y="2.3" width="10.4" height="7.4" rx="1" fill="none" stroke="#3d72c4" stroke-width="1.2"/><polyline points="1,3 6,7 11,3" fill="none" stroke="#3d72c4" stroke-width="1.2"/></svg>
          gtallis@brindlewave.vc
        </li>
        <li>
          <svg viewBox="0 0 12 12" aria-hidden="true"><circle cx="6" cy="6" r="5.2" fill="none" stroke="#3d72c4" stroke-width="1.2"/><ellipse cx="6" cy="6" rx="2.2" ry="5.2" fill="none" stroke="#3d72c4" stroke-width="1"/><line x1="0.8" y1="6" x2="11.2" y2="6" stroke="#3d72c4" stroke-width="1"/></svg>
          www.brindlewave.vc
        </li>
      </ul>
    </div>
    <div class="edge-band">
      <span class="band-blue"></span>
      <span class="band-black"></span>
    </div>
  </section>

</main>
</body>
</html>
```